BRV TAX & ACCOUNTING business card
Income tax, audit, bookkeeping, setup, training and services
Professional
Derek Lim Varga
48 Bexwell Drive
Toronto, ON M2K 4T8
brv_tax@quillmail.ca

```html
<!DOCTYPE html>
<html lang="en">
<head>
<meta charset="utf-8">
<title>BRV Tax &amp; Accounting — Business Card</title>
<link href="https://fonts.googleapis.com/css2?family=Montserrat:wght@800&family=Open+Sans:wght@400;700&display=swap" rel="stylesheet">
<style>
  :root {
    --brand-green: #6cc51f;
    --ink-black: #111111;
    --text-grey: #3a3a3a;
    --card-white: #ffffff;
    --backdrop: #e9e6e1;
  }
  html, body {
    margin: 0;
    width: 1200px;
    height: 914px;
    overflow: hidden;
    background: var(--backdrop);
  }
  .canvas {
    position: relative;
    width: 1200px;
    height: 914px;
  }
  .business-card {
    position: absolute;
    left: 80px;
    top: 160px;
    width: 1040px;
    height: 594px;
    background: var(--card-white);
    box-shadow: 0 10px 30px rgba(0,0,0,0.18);
    overflow: hidden;
    font-family: "Open Sans", Arial, sans-serif;
  }
  .accent-area {
    position: absolute;
    right: 0;
    top: 70px;
    width: 400px;
    height: 430px;
    background: linear-gradient(135deg, rgba(108,197,31,0) 0%, rgba(108,197,31,0.55) 55%, rgba(17,17,17,0.55) 100%);
  }
  .brand-name {
    position: absolute;
    left: 80px;
    top: 62px;
    margin: 0;
    color: var(--brand-green);
    font-family: "Montserrat", Arial, sans-serif;
    font-weight: 800;
    line-height: 1;
  }
  .brand-name .brand-initials {
    display: block;
    font-size: 86px;
    letter-spacing: 2px;
  }
  .brand-name .brand-tagline {
    display: block;
    font-size: 21px;
    margin-top: 6px;
    letter-spacing: 0.5px;
  }
  .contact-list {
    position: absolute;
    left: 46px;
    top: 268px;
    margin: 0;
    padding: 0;
    list-style: none;
    color: var(--text-grey);
    font-size: 17px;
    line-height: 25px;
  }
  .contact-item {
    display: flex;
    align-items: flex-start;
    gap: 10px;
  }
  .contact-icon {
    flex: 0 0 20px;
    width: 20px;
    height: 20px;
    margin-top: 2px;
  }
  .contact-item .indent {
    display: block;
  }
  .holder-name {
    position: absolute;
    right: 58px;
    bottom: 58px;
    margin: 0;
    color: var(--brand-green);
    font-weight: 700;
    font-size: 22px;
  }
</style>
</head>
<body>
<main class="canvas">
  <article class="business-card">
    <div class="accent-area" role="img" aria-label="Green and black curved accent band along the right edge"></div>

    <h1 class="brand-name">
      <span class="brand-initials">BRV</span>
      <span class="brand-tagline">TAX &amp; ACCOUNTING</span>
    </h1>

    <ul class="contact-list">
      <li class="contact-item">
        <svg class="contact-icon" viewBox="0 0 20 20" aria-hidden="true"><circle cx="10" cy="10" r="10" fill="var(--brand-green)"/><path d="M10 4.5a3.5 3.5 0 0 0-3.5 3.5c0 2.6 3.5 7 3.5 7s3.5-4.4 3.5-7A3.5 3.5 0 0 0 10 4.5z" fill="#fff"/><circle cx="10" cy="8" r="1.3" fill="var(--brand-green)"/></svg>
        <span>48 Bexwell Drive<span class="indent">Toronto, ON M2K 4T8</span></span>
      </li>
      <li class="contact-item">
        <svg class="contact-icon" viewBox="0 0 20 20" aria-hidden="true"><circle cx="10" cy="10" r="10" fill="var(--brand-green)"/><path d="M6.5 5h2l1 2.5-1.3 1a6 6 0 0 0 3.3 3.3l1-1.3 2.5 1v2a1 1 0 0 1-1 1A8.5 8.5 0 0 1 5.5 6a1 1 0 0 1 1-1z" fill="#fff"/></svg>
        <span>416-555-208-4</span>
      </li>
      <li class="contact-item">
        <svg class="contact-icon" viewBox="0 0 20 20" aria-hidden="true"><circle cx="10" cy="10" r="10" fill="var(--brand-green)"/><rect x="5" y="6.5" width="10" height="7" rx="1" fill="#fff"/><path d="M5.5 7l4.5 3.5L14.5 7" fill="none" stroke="var(--brand-green)" stroke-width="1.2"/></svg>
        <span>brv_tax@quillmail.ca</span>
      </li>
      <li class="contact-item">
        <svg class="contact-icon" viewBox="0 0 20 20" aria-hidden="true"><circle cx="10" cy="10" r="10" fill="var(--brand-green)"/><circle cx="10" cy="10" r="5" fill="none" stroke="#fff" stroke-width="1.3"/><path d="M5 10h10M10 5c-2 2.8-2 7.2 0 10M10 5c2 2.8 2 7.2 0 10" fill="none" stroke="#fff" stroke-width="1.1"/></svg>
        <span>www.brvtaxdesk.ca</span>
      </li>
    </ul>

    <p class="holder-name">Derek Lim Varga</p>
  </article>
</main>
</body>
</html>
```